Help our Crumb Parlour find our winning design! We're looking for a business card....

We’re a Crumb Parlour in NY specializing in custom-made cakes and unique desserts.
Our cakes combine flavor and art, each designed to match customer’s special event and theme.
We’d like a unique business card with a clean design that will combine French chic and artistic look & feel.
We’d like to differentiate ourselves from standard bakeries, please don’t offer cupcake images :-)
Our logo is peach-pink and brown and we’d love to use these colors ( . Another color that can be added is gold - or feel free to suggest!

Target Market(s)

Women, ages 25-55

Industry/Entity Type

Boutique

Contact Information for Business Card

Text on card:
Logo
Crumb Parlour by Dana Whitfield

www.xxxxxxxx.com
xxx@xxxxx.com
(516) xxx-xxxx
F – xxxxxxxxxx
IG - xxxxxxxxx

Font styles to use
Sans Serif
Script

Requirements
Must have
• Logo
• Clean look
• French chic and artistic look & feel.
Nice to have
• Damask pattern
Should not have
• Cupcake images

```html
<!DOCTYPE html>
<html lang="en">
<head>
<meta charset="utf-8">
<title>Crumb Parlour – Business Card</title>
<link rel="stylesheet" href="https://fonts.googleapis.com/css2?family=Great+Vibes&family=Open+Sans:wght@400;600&display=swap">
<style>
  :root {
    --backdrop: #2e2e2e;
    --card: #ffffff;
    --peach: #e8a58f;
    --peach-soft: #f6ddd3;
    --brown: #3a2a24;
    --ink: #4a3a34;
  }
  * { box-sizing: border-box; margin: 0; padding: 0; }
  html, body { width: 1200px; height: 900px; overflow: hidden; }
  body {
    background: var(--backdrop);
    font-family: "Open Sans", Arial, sans-serif;
    display: flex;
    flex-direction: column;
    align-items: center;
    justify-content: center;
    gap: 40px;
  }
  .card {
    position: relative;
    width: 700px;
    height: 400px;
    background: var(--card);
    box-shadow: 0 10px 30px rgba(0,0,0,.45);
    display: flex;
    flex-direction: column;
    align-items: center;
    color: var(--brown);
  }
  .card__frame {
    position: absolute;
    inset: 22px;
    width: calc(100% - 44px);
    height: calc(100% - 44px);
  }
  .flourish-area {
    position: absolute;
    left: 70px;
    right: 70px;
    border-radius: 50%;
    background: radial-gradient(ellipse at center, var(--peach-soft) 0%, rgba(246,221,211,.35) 55%, rgba(255,255,255,0) 75%);
  }
  .brand-name {
    position: relative;
    font-family: "Great Vibes", cursive;
    font-weight: 400;
    color: var(--brown);
    line-height: 1;
  }
  .tagline {
    position: relative;
    letter-spacing: .32em;
    text-transform: uppercase;
    color: var(--brown);
  }
  /* front */
  .card--front .flourish-area { top: 70px; height: 170px; }
  .card--front .brand-name { font-size: 78px; margin-top: 105px; }
  .card--front .tagline { font-size: 14px; margin-top: 14px; }
  .boutique-line {
    position: relative;
    display: flex;
    align-items: center;
    gap: 14px;
    margin-top: 20px;
    font-size: 17px;
    color: var(--ink);
  }
  .boutique-line__owner { font-family: "Great Vibes", cursive; font-size: 26px; color: var(--brown); }
  .ribbon { width: 22px; height: 16px; }
  /* back */
  .card--back .flourish-area { top: 40px; height: 190px; }
  .card--back .brand-name { font-size: 92px; margin-top: 80px; }
  .card--back .tagline { font-size: 16px; margin-top: 16px; }
  .contact {
    position: relative;
    margin-top: 46px;
    display: flex;
    flex-direction: column;
    align-items: center;
    gap: 8px;
    font-size: 17px;
    color: var(--ink);
  }
  .contact__row { display: flex; gap: 22px; }
  .contact__item { display: flex; align-items: center; gap: 7px; }
  .contact__icon { width: 16px; height: 16px; flex: none; }
  .contact__mark { width: 14px; height: 14px; background: var(--peach); flex: none; }
</style>
</head>
<body>

  <section class="card card--front" aria-label="Business card front">
    <svg class="card__frame" viewBox="0 0 656 356" preserveAspectRatio="none" aria-hidden="true">
      <path d="M12 1 H644 V12 H655 V344 H644 V355 H12 V344 H1 V12 H12 Z" fill="none" stroke="var(--peach)" stroke-width="1.6"/>
    </svg>
    <div class="flourish-area" role="img" aria-label="Peach calligraphic flourishes with a small tiered cake emblem"></div>
    <h1 class="brand-name">Crumb Parlour</h1>
    <p class="tagline">Handcrafted with love</p>
    <p class="boutique-line">
      <svg class="ribbon" viewBox="0 0 22 16" aria-hidden="true"><path d="M0 0 H22 L17 8 L22 16 H0 Z" fill="var(--peach)"/></svg>
      <span>Crumb Parlour by <span class="boutique-line__owner">Dana Whitfield</span></span>
      <svg class="ribbon" viewBox="0 0 22 16" aria-hidden="true"><path d="M22 0 H0 L5 8 L0 16 H22 Z" fill="var(--peach)"/></svg>
    </p>
  </section>

  <section class="card card--back" aria-label="Business card back">
    <div class="flourish-area" role="img" aria-label="Peach calligraphic flourishes with a small tiered cake emblem"></div>
    <h2 class="brand-name">Crumb Parlour</h2>
    <p class="tagline">Handcrafted with love</p>
    <div class="contact">
      <div class="contact__row">
        <span class="contact__item">
          <svg class="contact__icon" viewBox="0 0 16 16" aria-hidden="true"><path d="M2 6 C2 3 14 3 14 6 L11 7 L10 5.5 H6 L5 7 Z M4 8 H12 L13 13 H3 Z" fill="var(--peach)"/></svg>
          (516) 555-0182
        </span>
        <span class="contact__item">
          <svg class="contact__icon" viewBox="0 0 16 16" aria-hidden="true"><rect x="1" y="3.5" width="14" height="9" fill="var(--peach)"/><path d="M1.5 4 L8 9 L14.5 4" fill="none" stroke="#fff" stroke-width="1.2"/></svg>
          dana@CrumbParlourNY.com
        </span>
        <span class="contact__item">
          <svg class="contact__icon" viewBox="0 0 16 16" aria-hidden="true"><g fill="none" stroke="var(--peach)" stroke-width="1.3"><circle cx="8" cy="8" r="6.5"/><ellipse cx="8" cy="8" rx="2.8" ry="6.5"/><path d="M1.5 8 H14.5 M2.5 4.8 H13.5 M2.5 11.2 H13.5"/></g></svg>
          www.CrumbParlourNY.com
        </span>
      </div>
      <div class="contact__row">
        <span class="contact__item"><span class="contact__mark" aria-hidden="true"></span>CrumbParlourNYCakes</span>
        <span class="contact__item"><span class="contact__mark" aria-hidden="true"></span>CrumbParlourNYCakes</span>
      </div>
    </div>
  </section>

</body>
</html>
```